Luxury Wine Label for New Startup Winery

We need a wine label for our new winery startup. We have worked with a local designer but do not feel the resulting label / logo have the elevation required to present our brand as a luxury wine. Our winery is called "Harrowgate Vineyards" and we are focused on extremely high quality hand crafted artisan and estate wines from the Pacific Northwest.
We would like to see designs that utilize a tree line, or other imagery that represents the "Harrowgate" part of our company name. Another interesting feature could be wood grain.
A logo will be required based on your design so please design with this in mind:
This logo should be consistent with the wine bottle label design, and should be representative of our high end exclusive wine while giving a sense of place (Oregon/ Pacific Northwest.)
I will supply an image of the design we received from our local designer, PLEASE NOTE: in general we do like wood grain and tree line concepts but feel the execution was poorly done.
ATTN: Logo design should be suitable for use on: Bottles (Red wine/rose/white wine), Bussiness cards, vehicle signage, business signage, etc
P.S.:
If you have a design that is not outside the box we are still interested in seeing it.
Label is for a burgundy style bottle with a label height of 3.5 - 4" and a width of 3.5-4"
any label <= 4"x4" and >=3.5"x3.5" will be acceptable:
HOWEVER Width should be greater than or equal to height due to the bottle format
Target Market(s)
Wine enthusiasts with adequate discretionary budgets to afford $100 bottles of wine.
Industry/Entity Type
Wine / Winery
Requirements
Must have
- A sense of luxury, a feel of exclusivity, and a theme consistent with our product and brand name
Nice to have
- Tree line, wood grain or other wood themes. Serif fonts
Should not have
- anything cheesy, off topic, hard to read script fonts or anything that makes the label hard to read from a few feet away or too busy

```html
<!DOCTYPE html>
<html lang="en">
<head>
<meta charset="utf-8">
<title>Harrowgate Vineyards – Wine Label</title>
<link rel="stylesheet" href="https://fonts.googleapis.com/css2?family=Antonio:wght@300;400&family=Allura&display=swap">
<style>
  :root {
    --page-bg: #d6d6d6;
    --label-black: #0e0e0f;
    --marble-dark: #1b1b1d;
    --marble-mid: #3a3a3d;
    --marble-light: #55555a;
    --gold: #d9ad62;
    --gold-light: #f4d28c;
    --gold-deep: #9a6f2c;
    --oval-fill: #0b0b0c;
  }
  html, body {
    margin: 0;
    padding: 0;
    width: 1200px;
    height: 960px;
    overflow: hidden;
    background: var(--page-bg);
  }
  .label {
    position: absolute;
    left: 20px;
    top: 12px;
    width: 1160px;
    height: 936px;
    display: block;
    box-shadow: 0 6px 18px rgba(0,0,0,0.25);
  }
  .brand-title {
    font-family: "Antonio", "Arial Narrow", sans-serif;
    font-weight: 300;
    font-size: 84px;
    letter-spacing: 2px;
    fill: url(#goldText);
  }
  .tagline {
    font-family: "Allura", cursive;
    font-size: 40px;
    fill: var(--gold-light);
  }
  .volume-line {
    font-family: "Antonio", "Arial Narrow", sans-serif;
    font-weight: 400;
    font-size: 25px;
    letter-spacing: 1px;
    fill: var(--gold);
  }
</style>
</head>
<body>
<svg class="label" viewBox="0 0 1103 890" xmlns="http://www.w3.org/2000/svg" aria-label="Harrowgate Vineyards wine label">
  <defs>
    <linearGradient id="marble" x1="0" y1="0" x2="1" y2="1">
      <stop offset="0" stop-color="var(--marble-dark)"/>
      <stop offset="0.3" stop-color="var(--marble-mid)"/>
      <stop offset="0.5" stop-color="var(--marble-dark)"/>
      <stop offset="0.72" stop-color="var(--marble-light)"/>
      <stop offset="1" stop-color="var(--marble-dark)"/>
    </linearGradient>
    <linearGradient id="goldLine" x1="0" y1="0" x2="1" y2="1">
      <stop offset="0" stop-color="var(--gold-deep)"/>
      <stop offset="0.5" stop-color="var(--gold-light)"/>
      <stop offset="1" stop-color="var(--gold-deep)"/>
    </linearGradient>
    <linearGradient id="goldText" x1="0" y1="0" x2="0" y2="1">
      <stop offset="0" stop-color="var(--gold-light)"/>
      <stop offset="1" stop-color="var(--gold)"/>
    </linearGradient>
    <radialGradient id="vineyardScene" cx="0.5" cy="0.55" r="0.55">
      <stop offset="0" stop-color="#c9a055"/>
      <stop offset="0.55" stop-color="#6b5128"/>
      <stop offset="1" stop-color="var(--oval-fill)"/>
    </radialGradient>
    <path id="titleArc" d="M200,262 Q557,138 915,262"/>
  </defs>

  <!-- background -->
  <rect class="label-marble" x="0" y="0" width="1103" height="890" fill="url(#marble)"
        role="img" aria-label="Flowing black and grey marbled wave pattern"/>

  <!-- decorative gold curves -->
  <path class="gold-curve" d="M0,140 C200,100 420,130 560,95 C660,70 700,0 790,0" fill="none" stroke="url(#goldLine)" stroke-width="3"/>
  <path class="gold-curve" d="M940,0 C1000,60 1060,110 1103,150" fill="none" stroke="url(#goldLine)" stroke-width="3"/>

  <!-- outer frame -->
  <rect class="frame" x="22" y="30" width="1062" height="831" fill="none" stroke="url(#goldLine)" stroke-width="4"/>

  <!-- lower arched panel -->
  <path class="arch-panel" d="M27,858 V560 Q552,385 1077,560 V858" fill="none" stroke="url(#goldLine)" stroke-width="6"/>
  <path class="arch-panel" d="M40,855 V572 Q552,402 1064,572 V855" fill="none" stroke="url(#goldLine)" stroke-width="2"/>

  <!-- emblem oval -->
  <ellipse class="emblem-ring" cx="552" cy="443" rx="256" ry="146" fill="var(--oval-fill)" stroke="url(#goldLine)" stroke-width="7"/>
  <ellipse class="emblem-scene" cx="552" cy="448" rx="200" ry="112" fill="url(#vineyardScene)"
           role="img" aria-label="Gold engraved illustration of a hillside vineyard with an estate house and trees"/>

  <!-- title -->
  <text class="brand-title">
    <textPath href="#titleArc" startOffset="50%" text-anchor="middle">HARROWGATE VINEYARDS</textPath>
  </text>

  <!-- tagline -->
  <text class="tagline" x="552" y="678" text-anchor="middle">Premium Quality Hand Crafted</text>
  <text class="tagline" x="552" y="738" text-anchor="middle">Artisan and Estate Wines from the Pacific Northwest</text>

  <!-- volume & alcohol -->
  <text class="volume-line" x="552" y="829" text-anchor="middle">700ML │ 12,5 % ALCOHOL</text>
</svg>
</body>
</html>
```